Brisk Tutorium Website

We are looking for a new design of our website. The current website is www.brisktutorium.example. The company is the #1 pre-college math and science program in Orange County, CA. We would like to see designs that integrate our logo with a modern color scheme. We are also open for suggestions that could improve our logo. We would like a simple, minimal, clean, classy, and vibrant front-page user interface design that give the premium, modern, innovative, creative, and premier brand feel. We like the "New Retro Colors for the Web" as described here: http://www.pixel-layoutnook.example/en/layout-notes-2013/.

Target Market(s)

The target market is parents with K-12 students from a diverse population. Parents are well educated with family income > $150,000. Most of the decision makers are mothers from immigrate families: 30% Chinese, 30% Korean, 15% Indian, 24% White.

Industry/Entity Type

College

Requirements
Must have
• Must read our statement of differentiation at:
• http://brisktutorium.example/about-us
• Your design must be reflective of your understanding of the statements.
Nice to have
• The design should also be mobil friendly.
Should not have
• While most of our current classes are math, our company is expanding to include STEM (Science, Technology, Engineering, and Math) for gifted students. Therefore, the site should not be JUST a math education site.

```html
<!DOCTYPE html>
<html lang="en">
<head>
<meta charset="utf-8">
<title>Brisk Tutorium</title>
<link rel="stylesheet" href="https://fonts.googleapis.com/css2?family=Open+Sans:ital,wght@0,300;0,400;0,600;0,700;1,400;1,600;1,700&display=swap">
<style>
:root{
  --page:#ededed;
  --ink:#1e1e1e;
  --white:#ffffff;
  --header-dark:#5a3d22;
  --header-mid:#a9824f;
  --header-light:#e9dcc0;
  --tab:#e3d3ba;
  --events:#d9b48a;
  --news:#6fb59a;
  --location:#7dbde8;
  --about:#7a7d7a;
  --contact:#a79ca7;
  --scheduler:#9d98c9;
  --dash:#c5c3c0;
  --calendar:#f26b5e;
  --elearn-box:#e3e3e3;
  --home:#e8473a;
  --map-top:#fafafa;
  --map-bottom:#e4e4e4;
  --i1:#e06a3a;
  --i2:#2d5a9a;
  --i3:#2f8f4a;
  --i4:#e7a23c;
}
*{box-sizing:border-box;margin:0;padding:0}
html,body{width:703px;height:1200px;overflow:hidden}
body{background:var(--page);font-family:"Open Sans",Arial,sans-serif;color:var(--ink);position:relative}
.abs{position:absolute}
.header{left:17px;top:0;width:674px;height:230px;background:linear-gradient(160deg,var(--header-dark) 0%,var(--header-mid) 40%,var(--header-light) 75%,#f3ecdc 100%)}
.search{left:408px;top:16px;width:206px;height:18px;border-radius:9px;background:linear-gradient(#fff,#ddd);font-size:15px;line-height:18px;text-align:right;padding-right:6px}
.login{left:630px;top:16px;width:59px;height:18px;border-radius:9px;background:#fff;font-size:15px;line-height:18px;text-align:center}
.brand-title{right:12px;top:52px;font-size:62px;font-weight:300;color:#fff;line-height:1;white-space:nowrap}
.brand-sub{right:48px;top:126px;font-size:44px;font-weight:300;color:#fff;line-height:1;white-space:nowrap}
.tab{top:199px;height:31px;background:var(--tab);border-radius:14px 14px 0 0;font-weight:600;font-size:15px;text-align:center;line-height:33px;color:#222;white-space:nowrap}
.crumb{left:20px;top:234px;font-size:11px}
.crumb span{background:var(--home);color:#fff;font-style:italic;font-weight:700;border-radius:7px;padding:0 5px}
.panel-title{font-weight:300;color:#fff;line-height:1;white-space:nowrap}
.events{left:17px;top:252px;width:166px;height:114px;background:var(--events)}
.news{left:17px;top:370px;width:166px;height:116px;background:var(--news)}
.location{left:17px;top:492px;width:166px;height:368px;background:var(--location)}
.side-link{left:17px;width:166px;height:74px;color:#fff;font-size:34px;font-weight:300;line-height:74px;padding-left:8px;white-space:nowrap}
.more{font-size:8.5px;font-style:italic;text-align:right;white-space:nowrap}
.small{font-size:9px;line-height:11px}
.map{left:9px;top:108px;width:149px;height:172px;background:linear-gradient(var(--map-top),var(--map-bottom))}
.dash{left:187px;top:252px;width:384px;height:410px;background:var(--dash)}
.dash p{font-size:11.2px;line-height:13.6px}
.icon{top:161px;width:58px;height:58px;color:#fff;font-size:8px;font-weight:600;text-align:center;padding-top:43px;border:2px solid #fff;box-shadow:0 0 0 1px #888}
.calendar{left:576px;top:252px;width:115px;height:170px;background:var(--calendar)}
.cal-grid{left:14px;top:88px;display:grid;grid-template-columns:repeat(7,12px);font-size:8px;line-height:9.6px;text-align:center}
.cal-grid .today{background:#fff;border-radius:50%}
.why{left:187px;top:678px;width:389px;height:179px;background:var(--white);padding:8px 10px}
.why h2{font-weight:400;font-size:18.5px;margin-bottom:9px;white-space:nowrap}
.elearn h2{font-weight:400;font-size:16.5px;margin-bottom:14px;white-space:nowrap}
.why p,.elearn p{font-size:10.8px;line-height:12.8px}
.elearn{left:187px;top:860px;width:399px;height:194px;background:var(--elearn-box);padding:14px 12px}
.foot-logo{left:17px;top:1118px;width:247px;height:58px;background:var(--white);display:flex;align-items:center;padding-left:18px;gap:10px}
.foot-logo .dot{width:18px;height:18px;border-radius:50%;background:var(--i2)}
.foot-logo b{font-weight:400;font-size:21px;color:var(--i2);white-space:nowrap}
.foot-text{left:276px;top:1130px;font-size:12px;line-height:19px;white-space:nowrap}
</style>
</head>
<body>
<header class="abs header" role="img" aria-label="Photograph of an open book with fanned pages"></header>
<div class="abs search">|Search</div>
<div class="abs login">Login</div>
<div class="abs brand-title">Brisk Tutorium</div>
<div class="abs brand-sub">for gifted youth</div>

<nav>
  <div class="abs tab" style="left:22px;width:76px">Maths</div>
  <div class="abs tab" style="left:104px;width:76px">Physics</div>
  <div class="abs tab" style="left:184px;width:96px">Chemistry</div>
  <div class="abs tab" style="left:284px;width:78px">Biology</div>
  <div class="abs tab" style="left:366px;width:112px">Science Fair</div>
  <div class="abs tab" style="left:484px;width:98px">Fall 2013</div>
  <div class="abs tab" style="left:588px;width:103px">Results</div>
</nav>
<div class="abs crumb">&gt;&gt; <span>Home</span></div>

<section class="abs events">
  <div class="abs panel-title" style="left:8px;top:6px;font-size:34px">Events</div>
  <div class="abs" style="left:12px;top:46px;font-size:12px">MQC 8</div>
  <div class="abs" style="right:12px;top:46px;font-size:12px">TBD</div>
  <div class="abs" style="right:12px;top:62px;font-size:13px">2013-11-13</div>
  <div class="abs more" style="right:6px;top:96px">Click here to view all Events</div>
</section>

<section class="abs news">
  <div class="abs panel-title" style="left:8px;top:8px;font-size:34px">News</div>
  <div class="abs" style="left:6px;top:52px;width:156px;font-size:8px;line-height:10px">2013 College Matriculation List<br><span style="float:right">2013-06-02</span><br>Mira Lao and Owen Park Qualified for the 2013 National Physics Squad<br><span style="float:right">2013-05-20</span></div>
  <div class="abs more" style="right:6px;top:100px">Click here to view all News</div>
</section>

<section class="abs location">
  <div class="abs panel-title" style="left:4px;top:8px;font-size:35px">Location</div>
  <div class="abs small" style="left:6px;top:54px">Lindenhall College, Irvine<br>All weekend classes meet at<br>Lindenhall College,<br>Irvine.</div>
  <div class="abs map" role="img" aria-label="Street map showing the campus location"></div>
  <div class="abs small" style="left:6px;top:288px">Lindenhall College<br>1870 Lindenhall Way<br>Irvine, CA 92600-0000<br><br>Driving Directions to<br>Lindenhall College</div>
</section>

<div class="abs side-link" style="top:868px;background:var(--about)">About Us</div>
<div class="abs side-link" style="top:948px;background:var(--contact)">Contact</div>
<div class="abs side-link" style="top:1030px;background:var(--scheduler)">Sheduler</div>

<section class="abs dash">
  <div class="abs panel-title" style="left:8px;top:4px;font-size:34px">Dash Board</div>
  <div class="abs" style="left:10px;top:46px;width:366px">
    <p style="font-weight:700;font-style:italic">Math Olympiad and Problem Solving Training Programs</p>
    <p>Welcome to Brisk Tutorium for Gifted Youth. We provide after-school enrichment programs in math, physics, chemistry, biology, and computer science, mentor middle and high school science research projects, and offer college counseling to aspiring students in pursuing their college dreams. Please explore this website to learn more about our programs and our approach to gifted education.</p>
  </div>
  <div class="abs icon" style="left:52px;background:var(--i1)">eLearning</div>
  <div class="abs icon" style="left:125px;background:var(--i2)">Scheduler</div>
  <div class="abs icon" style="left:198px;background:var(--i3)">Newsletter</div>
  <div class="abs icon" style="left:271px;background:var(--i4)">Registration</div>
  <div class="abs" style="left:10px;top:226px;width:370px">
    <p>Click on eLearning to access our Online Learning Management<br>&nbsp;&nbsp;&nbsp;&nbsp;System for current students and families.</p>
    <p>Click on Scheduler to make an appointment online for qualifying<br>&nbsp;&nbsp;&nbsp;&nbsp;exams, gathering information, college counseling, or science<br>&nbsp;&nbsp;&nbsp;&nbsp;research meetings.</p>
    <p>Click on Newsletter to subscribe to our monthly newsletter -<br>&nbsp;&nbsp;&nbsp;&nbsp;The Brisk Learner.</p>
    <p>Click on Registration to sign up for our classes.</p>
  </div>
  <div class="abs" style="left:10px;top:350px;font-size:11.5px;font-weight:700;font-style:italic;line-height:19.5px">2013 - 2014 School Year Classes and Registration<br>2013 Summer Programs<br>New Student Registration</div>
  <div class="abs more" style="right:4px;top:392px;font-size:7.5px">Click Here to view complete Dash Board</div>
</section>

<aside class="abs calendar">
  <div class="abs" style="left:12px;top:4px;font-size:20px;color:#fff;font-weight:300">Calender</div>
  <div class="abs" style="left:18px;top:36px;font-size:17px;font-weight:400">26th Aug</div>
  <div class="abs" style="left:16px;top:64px;font-size:13px">&lt; August &gt;</div>
  <div class="abs cal-grid">
    <span>S</span><span>M</span><span>T</span><span>W</span><span>T</span><span>F</span><span>S</span>
    <span>28</span><span>29</span><span>30</span><span>31</span><span>1</span><span>2</span><span>3</span>
    <span>4</span><span>5</span><span>6</span><span>7</span><span>8</span><span>9</span><span>10</span>
    <span>11</span><span>12</span><span>13</span><span>14</span><span>15</span><span>16</span><span>17</span>
    <span>18</span><span>19</span><span>20</span><span>21</span><span>22</span><span>23</span><span>24</span>
    <span>25</span><span class="today">26</span><span>27</span><span>28</span><span>29</span><span>30</span><span>1</span>
  </div>
  <div class="abs more" style="left:18px;top:150px;text-align:left;line-height:10px">Click here to view<br>Complete calendar</div>
</aside>

<section class="abs why">
  <h2>Why Brisk Tutorium for Gifted Youth?</h2>
  <p>In 2006, Brisk Tutorium for Gifted Youth was the first academy to offer advanced math problem solving to gifted students in Orange County. With its roots in the Irvine math community and locations proximate to Coastal State University, Irvine and Lindenhall College, Brisk Tutorium for Gifted Youth combines California Standardized Mathematics Curriculum with math competitions and problem solving to help gifted students to discover their passion, develop their skills, and fulfill their college dreams. To learn more about our philosophy, history, statement of differentiation, and approach to gifted education, click here.</p>
</section>

<section class="abs elearn">
  <h2>Brisk eLearning - A Blended Learning Platform</h2>
  <p>We are pleased to announce the launch of Brisk Tutorium eLearning Center - an online community for students and parents to learn and share knowledge. With the eLearning Center, students have access to additional learning resources, can review classroom materials, download homework solutions, view grade reports, and share knowledge and communicate with other classmates in a safe and protected environment. Parents will be able to monitor their children's learning progress and participate in forum discussions related to gifted education and math talent development.</p>
  <p style="text-align:right;font-weight:700;font-style:italic;font-size:12px">Click here to learn more.</p>
</section>

<footer>
  <div class="abs foot-logo"><span class="dot"></span><b>Brisk Tutorium</b></div>
  <div class="abs foot-text">Copyright © 2000-2013 , Brisk Tutorium for Gifted Youth.<br>2250 Harbor Row, Suite 140 Irvine CA 92600. (949) 555-0142</div>
</footer>
</body>
</html>
```